Young judge needs a website to publish and to connect

I would like to have a website where I can publish my articles in public law. I am judge at the Alpine Civic Appeals Chamber. Therefore, the website must have a calm, friendly and fairly neutral design. Also, it should be mobile friendly and easy to use.

On my website, I want to

- publish articles such as https://www.quorvely.com/notes/how-win-court-tobias-wrenholt/ and get feedbacks from my colleagues
- generate interest for my project on 'Rules and Ballots - Notes from the Dais', a book that I would like to publish in 2020 and which brings together my publications on public law (http://www.statutewell.ch/content/english/profil/publikationen.html ).
- provide updates for my university courses on constitutional, administrative and international law.

For that purpose, I would kindly ask you to suggest a website that communicates a fresh approach to the work of a young judge in constitutional and administrative law. Please have in mind that I do not only sit on the bench, but that I also work in academia. Therefore, it should be suitable for an audience from both university and law practice. The website should replace the existing website on www.statutewell.ch that I designed when still working as a lawyer. Thank you.

Target Market(s)

Academica, law firms, courts

Industry/Entity Type

University

Contact Information for Business Card

Tobias Wrenholt
Judge
Alpine Civic Appeals Chamber
M +41 78 5XX 9X 2X

Logo Text

Notes from the Dais

Number of Pages Required

5+ page

Font styles to use
Sans Serif

Colors
0455a3

Requirements
Must have
• - a page where I can publish and get feedbacks
• - a page about my project on Rules and Ballots
• - a page where I can provide updates for my university courses on constitutional, administrative and international law
• - page where I can list current and planned projects
• - a collaborative, young and fresh approach
Nice to have
• - a page reserved for my colleagues at the Alpine Civic Appeals Chamber where I can alert them about to possibility to collaborate (if possibly password protected) and where they may suggest what to contribute to a specific project
Should not have
• anything which might to suggest that I want to make money with it, bragging or pretentious. Do not forget: I am judge, not a barrister.

```html
<!DOCTYPE html>
<html lang="en">
<head>
<meta charset="utf-8">
<title>Tobias Wrenholt</title>
<link rel="stylesheet" href="https://fonts.googleapis.com/css2?family=Open+Sans:wght@400;600;700&family=Open+Sans+Condensed:wght@700&family=Roboto+Slab:wght@400;700&display=swap">
<style>
:root{
  --brand:#0455a3;
  --brand-dark:#0b4a92;
  --sky:#2a8ef0;
  --sky-light:#3d9bf5;
  --red:#e8160c;
  --ink:#333;
  --muted:#777;
  --card:#f4f4f4;
  --white:#fff;
}
*{box-sizing:border-box;margin:0;padding:0}
html,body{width:1200px;height:2757px;overflow:hidden}
body{position:relative;font-family:"Open Sans",Arial,sans-serif;color:var(--ink);background:var(--white)}
.abs{position:absolute}

/* top bar */
.topbar{left:0;top:0;width:1200px;height:40px;background:var(--brand);color:var(--white);font-size:14px}
.topbar .address{left:75px;top:10px;display:flex;align-items:center;gap:8px}
.topbar .call{left:642px;top:10px}
.topbar .socials{left:826px;top:9px;display:flex;gap:11px}
.topbar .socials span{width:22px;height:22px;border-radius:50%;background:var(--sky-light);display:block}
.topbar .lang{left:985px;top:12px;font-size:11px}
.topbar .lang .active{color:#7cc0ff}

/* nav */
.nav{left:0;top:40px;width:1200px;height:87px;background:var(--white)}
.logo{left:75px;top:26px;font-family:"Roboto Slab",serif;font-weight:700;font-size:23px;color:var(--brand)}
.menu{left:381px;top:32px;display:flex;gap:0;font-size:15px;color:#222}
.menu a{color:inherit;text-decoration:none;margin-right:45px}
.menu a.current{color:var(--sky)}
.members{left:967px;top:26px;width:157px;height:35px;border-radius:18px;background:var(--red);color:var(--white);font-size:17px;text-align:center;line-height:35px}

/* hero */
.hero{left:0;top:127px;width:1200px;height:410px;background:linear-gradient(90deg,#2a2420 0%,#3b3028 40%,#1d1a18 100%)}
.hero-photo{left:60px;top:0;width:360px;height:410px;background:linear-gradient(180deg,#6d5f55,#3d3a3a);}
.hero .welcome{left:459px;top:148px;color:var(--white);font-family:"Open Sans Condensed","Open Sans",sans-serif;font-weight:700;font-size:30px}
.hero h1{left:457px;top:186px;color:#1b6ff0;font-family:"Open Sans Condensed","Open Sans",sans-serif;font-weight:700;font-size:52px;white-space:nowrap;line-height:1.1}
.hero .tagline{left:459px;top:244px;color:var(--white);font-size:18px}
.hero .arrow{top:182px;width:40px;height:40px;border-radius:50%;background:rgba(255,255,255,.15)}

/* features */
.feature{top:616px;height:196px;background:var(--sky);color:var(--white);text-align:center}
.feature.primary{background:var(--brand-dark);height:217px;border-bottom:8px solid var(--sky)}
.feature h2{margin-top:62px;font-family:"Open Sans Condensed","Open Sans",sans-serif;font-weight:700;font-size:25px}
.feature p{margin:14px auto 0;width:250px;font-size:13px;line-height:20px}
.feature-icon{top:568px;width:96px;height:96px;border-radius:50%;background:var(--brand-dark);display:flex;align-items:center;justify-content:center}

/* bio */
.bio{left:0;top:902px;width:1200px;height:399px;background:linear-gradient(90deg,#2a4f80,#1d3e6b 60%,#2a4a74)}
.bio-photo{left:78px;top:69px;width:264px;height:264px;border-radius:50%;background:linear-gradient(180deg,#c9c9cc,#8c8f96)}
.bio .divider{left:371px;top:67px;width:2px;height:258px;background:rgba(255,255,255,.6)}
.bio h2{left:408px;top:56px;color:var(--white);font-size:25px;font-weight:600}
.bio .role{left:408px;top:92px;color:var(--sky-light);font-size:15px}
.bio p{left:408px;top:128px;width:700px;color:#e8eef6;font-size:17px;line-height:31px}
.bio .more{left:408px;top:294px;width:110px;height:38px;border-radius:6px;background:var(--sky);color:var(--white);font-size:15px;font-weight:600;text-align:center;line-height:38px}

/* articles */
.section-title{left:0;top:1346px;width:1200px;text-align:center;color:var(--brand);font-family:"Open Sans Condensed","Open Sans",sans-serif;font-weight:700;font-size:26px}
.section-sub{left:0;top:1384px;width:1200px;text-align:center;color:#999;font-size:20px}
.card{width:313px;height:307px;background:var(--card);padding:24px 22px 0 22px}
.card h3{color:var(--brand);font-size:17px;font-weight:600;line-height:1}
.card .date{margin-top:6px;font-size:11px;color:var(--muted)}
.card p{margin-top:24px;font-size:13.5px;line-height:21px;color:#555;height:104px}
.card .read{margin-top:22px;display:inline-flex;align-items:center;gap:9px;height:27px;padding:0 6px 0 11px;background:var(--brand);color:var(--white);font-size:13.5px}
.card .read b{font-size:13px}
.card .meta{margin-top:25px;display:flex;gap:18px;font-size:11.5px;color:var(--muted)}
.card .meta span{display:flex;align-items:center;gap:5px}

/* pre-order */
.preorder{left:0;top:2152px;width:1200px;height:421px;background:var(--brand)}
.book{left:135px;top:38px;width:310px;height:346px;background:linear-gradient(135deg,#ff5a2a,#e8320e);transform:rotate(11deg)}
.preorder h2{left:485px;top:96px;color:var(--white);font-family:"Roboto Slab",serif;font-weight:400;font-size:40px}
.preorder .lead{left:485px;top:142px;color:var(--white);font-size:21px}
.field{top:201px;width:253px;height:44px;border:1.5px solid var(--white);border-radius:4px;color:var(--white);font-size:16px;line-height:41px;padding-left:17px}
.submit{left:485px;top:280px;width:226px;height:56px;background:var(--red);border-radius:4px;color:var(--white);font-family:"Open Sans Condensed","Open Sans",sans-serif;font-weight:700;font-size:26px;text-align:center;line-height:56px}

/* footer */
.footer-menu{left:0;top:2605px;width:1200px;text-align:center;font-size:16px;color:#444}
.footer-menu .current{color:var(--brand)}
.footer-socials{left:505px;top:2654px;display:flex;gap:15px}
.footer-socials span{width:29px;height:29px;border-radius:50%;border:2px solid var(--brand);display:block}
.copyright{left:0;top:2707px;width:1200px;text-align:center;font-size:15px;color:#888}
</style>
</head>
<body>

<header class="abs topbar">
  <div class="abs address">
    <svg width="11" height="15" viewBox="0 0 11 15"><path d="M5.5 0A5.5 5.5 0 0 0 0 5.5C0 9.6 5.5 15 5.5 15S11 9.6 11 5.5A5.5 5.5 0 0 0 5.5 0zm0 7.7a2.2 2.2 0 1 1 0-4.4 2.2 2.2 0 0 1 0 4.4z" fill="#fff"/></svg>
    Lindenmattweg 27 | PO Box 318 | 8047 Zurich | Switzerland
  </div>
  <div class="abs call">CALL: +41 44 580 12 64</div>
  <div class="abs socials"><span></span><span></span><span></span><span></span></div>
  <div class="abs lang">DEUTSCH &nbsp;| &nbsp;<span class="active">ENGLISH</span></div>
</header>

<nav class="abs nav">
  <div class="abs logo">TOBIAS WRENHOLT</div>
  <div class="abs menu">
    <a class="current">HOME</a><a>ABOUT</a><a>ARTICLES</a><a>PROJECT</a><a>COURSES</a><a>CONTACT</a>
  </div>
  <div class="abs members">ACA MEMBERS</div>
</nav>

<section class="abs hero">
  <div class="abs hero-photo" role="img" aria-label="Portrait of Tobias Wrenholt in a grey jacket against a courtroom backdrop with scales"></div>
  <div class="abs arrow" style="left:24px"><svg width="40" height="40"><path d="M23 13l-7 7 7 7" fill="none" stroke="#fff" stroke-width="2"/></svg></div>
  <div class="abs arrow" style="left:1134px"><svg width="40" height="40"><path d="M17 13l7 7-7 7" fill="none" stroke="#fff" stroke-width="2"/></svg></div>
  <div class="abs welcome">WELCOME TO</div>
  <h1 class="abs">TOBIAS WRENHOLT LAW FIRM</h1>
  <div class="abs tagline">in-house know-how of law firms by providing specialised expertise</div>
</section>

<section>
  <div class="abs feature" style="left:75px;width:355px">
    <h2>WHO WE ARE</h2>
    <p>Fusce vulputate tortor sed eros pellentesque pretium vivamus gravida mauris eget.</p>
  </div>
  <div class="abs feature primary" style="left:430px;width:340px">
    <h2>OUR PROJECTS</h2>
    <p>'Rules and Ballots - Notes from the Dais', a book that I would like to publish in 2020</p>
  </div>
  <div class="abs feature" style="left:770px;width:355px">
    <h2>OUR VISION</h2>
    <p>Maecenas rhoncus vulputate est, a finibus nisi posuere quisque vitae commodo mauris.</p>
  </div>
  <div class="abs feature-icon" style="left:206px">
    <svg width="46" height="46" viewBox="0 0 46 46"><path d="M12 6h24l-6 34H6z" fill="#fff"/><path d="M15 14h15M14 20h15M13 26h15" stroke="#0b4a92" stroke-width="2.5"/><path d="M36 6l4 6-6 34H8" fill="none" stroke="#fff" stroke-width="3"/></svg>
  </div>
  <div class="abs feature-icon" style="left:553px">
    <svg width="46" height="46" viewBox="0 0 46 46"><path d="M9 12h16l5 5v21H9z" fill="none" stroke="#fff" stroke-width="3"/><path d="M17 5h14l6 6v20H30" fill="none" stroke="#fff" stroke-width="3"/></svg>
  </div>
  <div class="abs feature-icon" style="left:900px">
    <svg width="50" height="40" viewBox="0 0 50 40"><path d="M2 20C10 8 18 4 25 4s15 4 23 16C40 32 32 36 25 36S10 32 2 20z" fill="#fff"/><circle cx="25" cy="20" r="9" fill="#0b4a92"/><circle cx="25" cy="20" r="4" fill="#fff"/></svg>
  </div>
</section>

<section class="abs bio">
  <div class="abs bio-photo" role="img" aria-label="Round portrait of Tobias Wrenholt"></div>
  <div class="abs divider"></div>
  <h2 class="abs">TOBIAS WRENHOLT RECHTSANWALT</h2>
  <div class="abs role">JUDGE, ALPINE CIVIC APPEALS CHAMBER</div>
  <p class="abs">statutewell.ch offers flexible legal outsourcing of Swiss administrative legal issues for business law firms. Its founder Tobias Wrenholt provides independent legal consulting services. Tobias's primary focus is on judicial review of administrative action and administrative procedure, but he also provides advice and legal opinions in health and higher education matters...</p>
  <div class="abs more">READ MORE</div>
</section>

<section>
  <h2 class="abs section-title">LATEST ARTICLES</h2>
  <div class="abs section-sub">Donec ullamcorper condimentum auctor donec laoreet sit amet tortor cursus mollis</div>

  <article class="abs card" style="left:110px;top:1461px">
    <h3>TEMPUS VEL LAOREET VITAE</h3>
    <div class="date">Published on October 24, 2015</div>
    <p>Etiam ut pretium mauris. Maecenas ligula rhoncus vulputate est, a finibus nisi amet posuere quisque vitae commodo mauris. Praesent tincidunt dignissim eros, posuere vestibulum quis.</p>
    <div class="read">Read article <b>&raquo;</b></div>
    <div class="meta"><span><svg width="13" height="12"><path d="M0 5h3v7H0zM4 5l3-5c2 0 2 2 1 4h4c1 0 1 1 1 2l-2 6H4z" fill="#666"/></svg>Like (48)</span><span><svg width="15" height="12"><ellipse cx="7.5" cy="5" rx="7.5" ry="5" fill="#666"/><path d="M3 8l-1 4 5-3z" fill="#666"/></svg>Comment (9)</span><span><svg width="14" height="12"><path d="M8 0l6 5-6 5V7C4 7 1 8 0 12 0 7 3 3 8 3z" fill="#666"/></svg>Share (5)</span></div>
  </article>
  <article class="abs card" style="left:445px;top:1461px">
    <h3>HOW TO WIN IN COURT</h3>
    <div class="date">Published on October 24, 2015</div>
    <p>Whereas court proceedings tend to be complicated, judges are not. In fact, they are rather simple creatures. This is why they like it simple. And this is why it is not always that hard to win in court...</p>
    <div class="read">Read article <b>&raquo;</b></div>
    <div class="meta"><span><svg width="13" height="12"><path d="M0 5h3v7H0zM4 5l3-5c2 0 2 2 1 4h4c1 0 1 1 1 2l-2 6H4z" fill="#666"/></svg>Like (48)</span><span><svg width="15" height="12"><ellipse cx="7.5" cy="5" rx="7.5" ry="5" fill="#666"/><path d="M3 8l-1 4 5-3z" fill="#666"/></svg>Comment (9)</span><span><svg width="14" height="12"><path d="M8 0l6 5-6 5V7C4 7 1 8 0 12 0 7 3 3 8 3z" fill="#666"/></svg>Share (5)</span></div>
  </article>
  <article class="abs card" style="left:779px;top:1461px">
    <h3>VIVAMUS GRAVIDA MAURIS EGET</h3>
    <div class="date">Published on October 24, 2015</div>
    <p>Proin ac laoreet dui, a rhoncus urna amet Phasellus a pharetra nibh. Integer at risus malesuada felis dignissim rhoncus ut nec quam.Suspendisse orci urna, tempus vel turpis vel, tincidunt egestas ligula.</p>
    <div class="read">Read article <b>&raquo;</b></div>
    <div class="meta"><span><svg width="13" height="12"><path d="M0 5h3v7H0zM4 5l3-5c2 0 2 2 1 4h4c1 0 1 1 1 2l-2 6H4z" fill="#666"/></svg>Like (48)</span><span><svg width="15" height="12"><ellipse cx="7.5" cy="5" rx="7.5" ry="5" fill="#666"/><path d="M3 8l-1 4 5-3z" fill="#666"/></svg>Comment (9)</span><span><svg width="14" height="12"><path d="M8 0l6 5-6 5V7C4 7 1 8 0 12 0 7 3 3 8 3z" fill="#666"/></svg>Share (5)</span></div>
  </article>

  <article class="abs card" style="left:106px;top:1794px">
    <h3>TEMPUS VEL LAOREET VITAE</h3>
    <div class="date">Published on October 24, 2015</div>
    <p>Etiam ut pretium mauris. Maecenas ligula rhoncus vulputate est, a finibus nisi amet posuere quisque vitae commodo mauris. Praesent tincidunt dignissim eros, posuere vestibulum quis.</p>
    <div class="read">Read article <b>&raquo;</b></div>
    <div class="meta"><span><svg width="13" height="12"><path d="M0 5h3v7H0zM4 5l3-5c2 0 2 2 1 4h4c1 0 1 1 1 2l-2 6H4z" fill="#666"/></svg>Like (48)</span><span><svg width="15" height="12"><ellipse cx="7.5" cy="5" rx="7.5" ry="5" fill="#666"/><path d="M3 8l-1 4 5-3z" fill="#666"/></svg>Comment (9)</span><span><svg width="14" height="12"><path d="M8 0l6 5-6 5V7C4 7 1 8 0 12 0 7 3 3 8 3z" fill="#666"/></svg>Share (5)</span></div>
  </article>
  <article class="abs card" style="left:441px;top:1794px">
    <h3>HOW TO WIN IN COURT</h3>
    <div class="date">Published on October 24, 2015</div>
    <p>Whereas court proceedings tend to be complicated, judges are not. In fact, they are rather simple creatures. This is why they like it simple. And this is why it is not always that hard to win in court...</p>
    <div class="read">Read article <b>&raquo;</b></div>
    <div class="meta"><span><svg width="13" height="12"><path d="M0 5h3v7H0zM4 5l3-5c2 0 2 2 1 4h4c1 0 1 1 1 2l-2 6H4z" fill="#666"/></svg>Like (48)</span><span><svg width="15" height="12"><ellipse cx="7.5" cy="5" rx="7.5" ry="5" fill="#666"/><path d="M3 8l-1 4 5-3z" fill="#666"/></svg>Comment (9)</span><span><svg width="14" height="12"><path d="M8 0l6 5-6 5V7C4 7 1 8 0 12 0 7 3 3 8 3z" fill="#666"/></svg>Share (5)</span></div>
  </article>
  <article class="abs card" style="left:775px;top:1794px">
    <h3>VIVAMUS GRAVIDA MAURIS EGET</h3>
    <div class="date">Published on October 24, 2015</div>
    <p>Proin ac laoreet dui, a rhoncus urna amet Phasellus a pharetra nibh. Integer at risus malesuada felis dignissim rhoncus ut nec quam.Suspendisse orci urna, tempus vel turpis vel, tincidunt egestas ligula.</p>
    <div class="read">Read article <b>&raquo;</b></div>
    <div class="meta"><span><svg width="13" height="12"><path d="M0 5h3v7H0zM4 5l3-5c2 0 2 2 1 4h4c1 0 1 1 1 2l-2 6H4z" fill="#666"/></svg>Like (48)</span><span><svg width="15" height="12"><ellipse cx="7.5" cy="5" rx="7.5" ry="5" fill="#666"/><path d="M3 8l-1 4 5-3z" fill="#666"/></svg>Comment (9)</span><span><svg width="14" height="12"><path d="M8 0l6 5-6 5V7C4 7 1 8 0 12 0 7 3 3 8 3z" fill="#666"/></svg>Share (5)</span></div>
  </article>
</section>

<section class="abs preorder">
  <div class="abs book" role="img" aria-label="Red-orange book cover of Rules and Ballots by Tobias Wrenholt"></div>
  <h2 class="abs">RULES AND BALLOTS PRE-ORDER!</h2>
  <div class="abs lead">Enter your name and mobile number below</div>
  <div class="abs field" style="left:485px">Name</div>
  <div class="abs field" style="left:758px">Email address</div>
  <div class="abs submit">SUBMIT NOW</div>
  <svg class="abs" style="left:722px;top:268px" width="150" height="80" viewBox="0 0 150 80">
    <path d="M145 8C120 50 70 68 12 58" fill="none" stroke="#fff" stroke-width="4" stroke-linecap="round"/>
    <path d="M30 40L8 57l26 12" fill="none" stroke="#fff" stroke-width="4" stroke-linecap="round" stroke-linejoin="round"/>
  </svg>
</section>

<footer>
  <div class="abs footer-menu"><span class="current">HOME</span> &nbsp;| &nbsp;ABOUT &nbsp;| &nbsp;ARTICLES &nbsp;| &nbsp;PROJECT &nbsp;| &nbsp;COURSES &nbsp;| &nbsp;CONTACT</div>
  <div class="abs footer-socials"><span></span><span></span><span></span><span></span></div>
  <div class="abs copyright">Copyright © 2017 statutewell. All rights reserved.</div>
</footer>

</body>
</html>
```